The Quick Guard Privacy Handbook

A book cover. The book will be marketed as a promotional item for financial advisors, financial planners, independent insurance agents, bankers, and any professional who views their role as guardian of their clients assets and helping them manage risk.

```html
<!DOCTYPE html>
<html lang="en">
<head>
<meta charset="utf-8">
<title>The Quick Guard Privacy Handbook — Cover</title>
<link href="https://fonts.googleapis.com/css2?family=Fira+Sans+Extra+Condensed:ital,wght@0,500;0,600;0,700;0,800;1,600&display=swap" rel="stylesheet">
<style>
  :root {
    --backdrop: #d3d3d3;
    --paper: #ffffff;
    --ink: #111111;
    --gold-dark: #b08d07;
    --gold-light: #ecc81a;
    --silver-dark: #9a9ea3;
    --silver-mid: #c9ccd0;
    --silver-light: #eef0f1;
  }
  * { box-sizing: border-box; margin: 0; padding: 0; }
  html, body {
    width: 1200px;
    height: 849px;
    overflow: hidden;
    background: var(--backdrop);
  }
  .canvas {
    position: relative;
    width: 1200px;
    height: 849px;
  }
  .cover {
    position: absolute;
    left: 330px;
    top: 19px;
    width: 540px;
    height: 810px;
    background: var(--paper);
    overflow: hidden;
    font-family: "Fira Sans Extra Condensed", "Arial Narrow", sans-serif;
    color: var(--ink);
  }
  .title-lead {
    position: absolute;
    top: 76px;
    left: 58px;
    right: 58px;
    display: flex;
    align-items: center;
    gap: 18px;
  }
  .title-lead .rule {
    flex: 1;
    height: 2px;
    background: linear-gradient(90deg, var(--gold-dark), var(--gold-light), var(--gold-dark));
  }
  .title-lead .word {
    font-weight: 800;
    font-size: 44px;
    line-height: 1;
  }
  .title-main {
    position: absolute;
    top: 114px;
    left: 0;
    right: 0;
    text-align: center;
    font-weight: 800;
    font-size: 84px;
    line-height: 1;
    letter-spacing: 1px;
    white-space: nowrap;
  }
  .title-divider {
    position: absolute;
    top: 208px;
    left: 54px;
    right: 54px;
    height: 2px;
    background: linear-gradient(90deg, var(--gold-dark), var(--gold-light), var(--gold-dark));
  }
  .title-sub {
    position: absolute;
    top: 215px;
    left: 0;
    right: 0;
    text-align: center;
    font-weight: 700;
    font-size: 42px;
    line-height: 1;
    letter-spacing: 2.5px;
    white-space: nowrap;
  }
  .tagline {
    position: absolute;
    top: 263px;
    left: 52px;
    right: 52px;
    height: 41px;
    border-radius: 9px;
    background: linear-gradient(90deg, var(--gold-dark), var(--gold-light) 50%, var(--gold-dark));
    display: flex;
    align-items: center;
    justify-content: center;
    font-style: italic;
    font-weight: 600;
    font-size: 22px;
  }
  .motto {
    position: absolute;
    top: 318px;
    left: 0;
    right: 0;
    text-align: center;
    font-weight: 600;
    font-size: 25px;
    line-height: 1.15;
    letter-spacing: 0.9px;
  }
  .artwork {
    position: absolute;
    left: 0;
    right: 0;
    top: 416px;
    bottom: 0;
    background: linear-gradient(180deg, var(--silver-light) 0%, var(--silver-mid) 45%, var(--silver-dark) 70%, var(--silver-light) 100%);
  }
</style>
</head>
<body>
  <main class="canvas">
    <section class="cover">
      <div class="title-lead">
        <span class="rule"></span>
        <span class="word">THE</span>
        <span class="rule"></span>
      </div>
      <h1 class="title-main">QUICK GUARD</h1>
      <div class="title-divider"></div>
      <h2 class="title-sub">PRIVACY HANDBOOK</h2>
      <p class="tagline">Protect Yourself and Your Family in the AI Age</p>
      <p class="motto">IT’S BETTER TO HAVE IT AND NOT NEEDED IT<br>THAN NEED IT AND NOT HAVE IT.</p>
      <div class="artwork" role="img" aria-label="Photograph of a chrome stopwatch with a white dial and a black hand just past 60"></div>
    </section>
  </main>
</body>
</html>
```